IT Services Business Card Design

We require a business card design for an IT services company called RT Program Freightworks.

We specialize in taking an organisations software and readying it for deployment to new environments (e.g. Zen qa to Zen 4). This process is termed application packaging. This is not the same as putting things in boxes but I am happy to use boxes as a pun icon ;-) This is our second step in branding, we currently have a new logo and our poor excuse of a website is next to be updated but it contains information on who we are and what we cover at rtprogramfreightworks.example

We are looking for a fun, modern but stylish and professional looking design.

I have attached the logo in multiple formats including vector formats (and the fonts that created the logo if required)
Updates

Thanks to all the designers so far, some great designs in there.  I will be selecting a card design on the deadline date. 

However, there is still time to submit some more designs.  The majority of the ones I have so far are typical simplistic designs that we have all seen before and I have enough of those to choose from now.  If you wish to submit any more designs, please submit somthing unusual to grab our attention.

Target Market(s)

Project executives of large organisations looking for Panecraft migrations

Industry/Entity Type

Software

Requirements
Must have
• Want to show company name, contact name, title, main number, contact number, fax number, email address and website address. I do not want to show the address.
Must use the attached logo, retaining the colours in them.

This has to be a double-sided design. I will be using lark.example and will be selecting their rounded corner business card design.

Their templates and design requirements (sizing etc.) can be found here: http://uk.lark.example/help/faq/templates-and-guidelines.html

Happy for company name or website to be on either side of the card.

This design has to be original and not used before for another company

Would like to style it around the business colours in the logo
Nice to have
• Lark.example has an option for multiple card designs to appear on the back. If this is possible in the budget and time you have and you have a design(s) that work with that but carry the same style and theme, that would be nice to see but not necessary.
Should not have
• We do not want to put a postal address on the cards

```html
<!DOCTYPE html>
<html lang="en">
<head>
<meta charset="utf-8">
<title>RT Program Freightworks – Business Card</title>
<link rel="stylesheet" href="https://fonts.googleapis.com/css2?family=Didact+Gothic&family=Open+Sans:wght@400;600&display=swap">
<style>
  :root {
    --page: #ffffff;
    --card-light: #ffffff;
    --card-dark: #2e322d;
    --brand-blue: #4a63ad;
    --brand-blue-deep: #3f58a3;
    --brand-blue-soft: #8ea2d8;
    --ink-grey: #5b5955;
    --ink-dark: #3a3a3a;
    --ink-light: #d6d6d6;
    --url-grey: #c4c6c2;
  }
  html, body {
    margin: 0;
    padding: 0;
    width: 1200px;
    height: 900px;
    overflow: hidden;
    background: var(--page);
  }
  .canvas {
    position: relative;
    width: 1200px;
    height: 900px;
  }
  .card {
    position: absolute;
    width: 476px;
    height: 312px;
    border-radius: 18px;
    box-shadow: 0 4px 10px rgba(0, 0, 0, 0.22);
    overflow: hidden;
  }
  .card--front {
    left: 144px;
    top: 108px;
    background: var(--card-light);
  }
  .card--back {
    left: 594px;
    top: 472px;
    background: var(--card-dark);
  }
  .brand-field {
    position: absolute;
    left: 292px;
    top: 30px;
    right: 0;
    bottom: 0;
    border-top-left-radius: 14px;
    background:
      linear-gradient(180deg, rgba(255,255,255,0) 55%, rgba(255,255,255,0.25) 100%),
      linear-gradient(135deg, var(--brand-blue-deep) 0%, var(--brand-blue) 45%, var(--brand-blue-soft) 100%);
  }
  .wordmark {
    position: absolute;
    display: flex;
    align-items: center;
    gap: 10px;
    font-family: "Didact Gothic", sans-serif;
    white-space: nowrap;
  }
  .wordmark__dot {
    border-radius: 50%;
    background: var(--brand-blue);
    flex: none;
  }
  .card--front .wordmark {
    left: 32px;
    top: 36px;
    font-size: 21px;
    color: var(--ink-grey);
  }
  .card--front .wordmark__dot {
    width: 22px;
    height: 22px;
  }
  .card--back .wordmark {
    left: 0;
    right: 0;
    justify-content: center;
    top: 110px;
    font-size: 30px;
    color: var(--ink-light);
  }
  .card--back .wordmark__dot {
    width: 34px;
    height: 34px;
  }
  .holder {
    position: absolute;
    left: 34px;
    top: 134px;
    font-family: "Didact Gothic", sans-serif;
  }
  .holder__name {
    margin: 0;
    font-size: 15px;
    color: var(--ink-dark);
  }
  .holder__title {
    margin: 2px 0 0;
    font-family: "Open Sans", sans-serif;
    font-weight: 600;
    font-size: 15px;
    color: var(--brand-blue);
  }
  .contacts {
    position: absolute;
    left: 34px;
    top: 210px;
    margin: 0;
    padding: 0;
    list-style: none;
    font-family: "Didact Gothic", sans-serif;
    font-size: 12px;
    line-height: 18px;
    color: var(--ink-dark);
  }
  .contacts__label {
    display: inline-block;
    width: 18px;
    font-family: "Open Sans", sans-serif;
    font-weight: 600;
    color: var(--brand-blue);
  }
  .web {
    position: absolute;
    left: 0;
    right: 0;
    top: 255px;
    margin: 0;
    text-align: center;
    font-family: "Open Sans", sans-serif;
    font-size: 19px;
    color: var(--url-grey);
  }
</style>
</head>
<body>
<main class="canvas">

  <section class="card card--front" aria-label="Card front">
    <div class="brand-field" role="img" aria-label="Large brand-blue decorative graphic area"></div>

    <div class="wordmark">
      <span class="wordmark__name">RT Program Freightworks</span>
      <span class="wordmark__dot"></span>
    </div>

    <div class="holder">
      <p class="holder__name">Your Name</p>
      <p class="holder__title">Managing Director</p>
    </div>

    <ul class="contacts">
      <li><span class="contacts__label">T</span>0845 210 7788</li>
      <li><span class="contacts__label">M</span>07700 900456</li>
      <li><span class="contacts__label">F</span>0872 555 0193</li>
      <li><span class="contacts__label">E</span>Enquiries@RTProgramFreightworks.example</li>
    </ul>
  </section>

  <section class="card card--back" aria-label="Card back">
    <div class="wordmark">
      <span class="wordmark__name">RT Program Freightworks</span>
      <span class="wordmark__dot"></span>
    </div>
    <p class="web">www.rtprogramfreightworks.example</p>
  </section>

</main>
</body>
</html>
```